CTWI application splash screen

We need a 1024x768 image for use as an application splash screen.
The image will be displayed full screen on an 10 inch industrial PC 1024x768 screen while our application is launching. The image should convey that the application is "Waiting for connection to Wi-Fi access point..." and include a graphic of the industrial PC connected to the access point via an Ethernet cable. A list of troubleshooting steps should be included at the bottom of the image. The troubleshooting steps should not be the main focus of the image and should be shown in a smaller font (but still readable at 1024x768 displayed on a 10 inch screen).
I will include a mock up of the general idea of what we are looking for as well as image files for the industrial PC, a screenshot of our application to show on the PC's screen and the AP.
For general look and feel and a sense of corporate branding please review our website https://corvanetillageworks.com/. The splash screen should reflect corporate branding.
Target Market(s)
Users of our application
Industry/Entity Type
Agriculture

```html
<!DOCTYPE html>
<html lang="en">
<head>
<meta charset="UTF-8">
<title>CTWI – Waiting for Wi-Fi access point</title>
<link href="https://fonts.googleapis.com/css2?family=Poppins:wght@400;500&display=swap" rel="stylesheet">
<style>
  :root {
    --brand-green: #2bb673;
    --ink: #2f2f2f;
    --ink-soft: #444444;
    --paper: #ffffff;
    --device-dark: #1c1c1c;
    --ap-white: #f3f5f4;
  }
  * { box-sizing: border-box; margin: 0; padding: 0; }
  html, body {
    width: 1200px;
    height: 1200px;
    overflow: hidden;
    background: var(--paper);
    font-family: "Poppins", sans-serif;
  }
  .splash {
    position: absolute;
    left: 0;
    top: 150px;
    width: 1200px;
    height: 900px;
    background: var(--paper);
  }
  .hero {
    position: absolute;
    left: 0;
    top: 0;
    width: 1200px;
    height: 726px;
    background: var(--brand-green);
    border-radius: 0 0 135px 135px;
    overflow: hidden;
  }
  .hero__title {
    position: absolute;
    left: 0;
    right: 0;
    top: 254px;
    text-align: center;
    color: var(--paper);
    font-weight: 500;
    font-size: 35px;
    letter-spacing: 0.1px;
    white-space: nowrap;
  }
  .hero__diagram {
    position: absolute;
    left: 0;
    top: 0;
    width: 1200px;
    height: 726px;
  }
  .trouble {
    position: absolute;
    left: 53px;
    top: 752px;
    color: var(--ink);
  }
  .trouble__tag {
    display: inline-block;
    background: var(--brand-green);
    color: var(--paper);
    font-size: 11px;
    line-height: 22px;
    height: 22px;
    padding: 0 11px;
    border-radius: 7px;
  }
  .trouble__note {
    display: flex;
    align-items: center;
    gap: 4px;
    font-size: 10.8px;
    margin-top: 8px;
    margin-left: 6px;
  }
  .trouble__note + .trouble__note { margin-top: 5px; }
  .trouble__icon {
    width: 12px;
    height: 12px;
    flex: none;
  }
  .trouble__steps {
    list-style: none;
    margin-left: 22px;
    margin-top: 3px;
    font-size: 9.2px;
    line-height: 11.3px;
    color: var(--ink-soft);
    white-space: nowrap;
  }
  .trouble__steps li::before {
    content: "•";
    margin-right: 5px;
  }
  .brand {
    position: absolute;
    left: 1020px;
    top: 800px;
    display: flex;
    align-items: center;
    gap: 8px;
    color: var(--brand-green);
    font-weight: 500;
    font-size: 30px;
  }
  .brand__dot {
    width: 18px;
    height: 18px;
    border-radius: 50%;
    background: var(--brand-green);
  }
</style>
</head>
<body>
<main class="splash">
  <section class="hero">
    <svg class="hero__diagram" viewBox="0 0 1200 726" xmlns="http://www.w3.org/2000/svg">
      <path class="cable" d="M427 496 V509 Q427 517 435 517 H722 Q730 517 731 509 L733 498 Q735 490 745 490 H875"
            fill="none" stroke="#ffffff" stroke-width="2" stroke-dasharray="7 4"/>
      <rect class="industrial-pc" role="img" aria-label="Industrial PC showing the application's bar chart screen"
            x="266" y="369" width="176" height="128" rx="8" fill="var(--device-dark)"/>
      <rect class="access-point" role="img" aria-label="Outdoor Wi-Fi access point with two antennas"
            x="875" y="364" width="16" height="135" rx="4" fill="var(--ap-white)"/>
    </svg>
    <h1 class="hero__title">Waiting for connection to Wi-Fi access point...</h1>
  </section>

  <section class="trouble">
    <span class="trouble__tag">Troubleshooting steps:</span>
    <p class="trouble__note">
      <svg class="trouble__icon" viewBox="0 0 12 12"><circle cx="6" cy="6" r="5.2" fill="none" stroke="var(--brand-green)" stroke-width="1"/><rect x="5.4" y="2.8" width="1.2" height="4.4" fill="var(--brand-green)"/><rect x="5.4" y="8" width="1.2" height="1.2" fill="var(--brand-green)"/></svg>
      This screen should only be visible for a short time on boot.
    </p>
    <p class="trouble__note">
      <svg class="trouble__icon" viewBox="0 0 12 12"><circle cx="6" cy="6" r="5.2" fill="none" stroke="var(--brand-green)" stroke-width="1"/><rect x="5.4" y="2.8" width="1.2" height="4.4" fill="var(--brand-green)"/><rect x="5.4" y="8" width="1.2" height="1.2" fill="var(--brand-green)"/></svg>
      If this screen stays visible for more than a minute:
    </p>
    <ul class="trouble__steps">
      <li>Verify that the Wi-Fi Access Point (AP) powers up when this system does (indicated by a green light on the side of the AP).</li>
      <li>Check the Ethernet cable between this system and the AP for damage, and replace it if necessary.</li>
      <li>Power-cycle this system and wait for it to reboot fully.</li>
      <li>If the issue persists, contact CTWI support for further assistance.</li>
    </ul>
  </section>

  <div class="brand">
    <span class="brand__dot"></span>
    <span class="brand__name">CTWI</span>
  </div>
</main>
</body>
</html>
```